Flyer-Design für Open Workspace Lösung
Zielgruppe
Was machen wir? Open Workspace Lösung für Ärzte und Psychotherapeuten.
Zielgruppe: Unser Angebot richtet sich an Ärzte, Psychologen, Psychotherapeuten, Heilpraktiker für Psychotherapie (HeilprG) sowie Coaches und Supervisoren mit vergleichbarem und zertifiziertem Hintergrund. Darüber hinaus stehen die Räume auch für Seminare, Workshops oder Gruppenangebote zur Verfügung.
Aufgabenstellung
1. Die Word-Skizze ist ein Entwurf, der gerne verändert werden kann.
2. Das Foto in der oberen Hälfte ist ein Platzhalter. Es ist zwar real aber wir haben leider noch kein gutes Foto der fertigen Räume. Daher sollte, falls ein Bild verwendet wird, eine bearbeitbare Version mitgeliefert werden, damit wir das Bild noch austauschen können. Es muss kein Bild im Flyer verwendet werden, kann aber.
3. Unser Logo sollte auf den Flyer kommen. Es gibt das Logo mit und ohne Text. Beide hängen wir als Datei mit an.
4. Wir haben eine Website: www.praxis-sonnenwiese.de
Der Flyer sollte zu dieser passen. Die Schriftart der Website ist font-famliy: 'Lato', sans-serif und sollte verwendet werden.
5. Die Farbe (türkis) ist vorgegeben. Die Definition ist: #0CE0AE
Die Grautöne der Website sind folgende: #444444, #555444, #5A5A5A, #888888, #CCCCCC #F4F4F4
6. wir hätten gerne einen one-pager, den man als Werbung an Emails anhängen und im Internet veröffentlichen kann und einen Flyer, der ausgedruckt ausliegen kann

```html
<!DOCTYPE html>
<html lang="de">
<head>
<meta charset="utf-8">
<title>Seminarräume – Preise und FAQ</title>
<link href="https://fonts.googleapis.com/css2?family=Outfit:wght@300;400;500&display=swap" rel="stylesheet">
<style>
  :root {
    --turquoise: #0CE0AE;
    --grey-dark: #5A5A5A;
    --grey-text: #555555;
    --white: #FFFFFF;
    --black: #111111;
  }
  * { margin: 0; padding: 0; box-sizing: border-box; }
  html, body { width: 1200px; height: 848px; overflow: hidden; background: var(--white); }
  body { position: relative; font-family: "Outfit", sans-serif; color: var(--grey-text); }

  .panel { position: absolute; top: 0; height: 848px; width: 400px; }
  .panel--rooms { left: 0; }
  .panel--prices { left: 400px; width: 401px; background: var(--turquoise); }
  .panel--faq { left: 801px; width: 399px; }

  .abs { position: absolute; left: 0; right: 0; text-align: center; }

  .panel-title { font-weight: 500; font-size: 20px; line-height: 24px; color: var(--grey-dark); letter-spacing: -0.2px; }
  .title-rule { position: absolute; left: 162px; width: 77px; top: 75px; height: 2px; background: var(--grey-dark); }

  .body-text { font-weight: 300; font-size: 15px; line-height: 16.1px; color: var(--grey-text); }
  .rooms-text { padding: 0 14px; }
  .faq-text { padding: 0 10px; }

  .room-label { font-weight: 500; font-size: 20px; line-height: 24px; color: var(--grey-dark); letter-spacing: -0.2px; }
  .room-photo { position: absolute; left: 0; width: 400px; height: 130px; }
  .room-photo--one { top: 481px; background: linear-gradient(100deg, #d9d2c2 0%, #b6753d 30%, #d8cfc3 55%, #c9b89f 80%, #6b4630 100%); }
  .room-photo--two { top: 661px; background: linear-gradient(100deg, #e3e6de 0%, #b77a36 25%, #d7d2c8 55%, #c8b08c 80%, #7a5638 100%); }

  .price-box { position: absolute; left: 93px; width: 216px; height: 90px; background: var(--white); color: var(--black); text-align: center; font-weight: 400; }
  .price-day { font-size: 21px; line-height: 22px; margin-top: 6px; }
  .price-time { font-size: 15px; line-height: 17px; }
  .price-amount { font-size: 32px; line-height: 36px; }
  .price-box--combo .price-amount { margin-top: 17px; }
  .price-box--triple .price-day { line-height: 22px; }
  .price-box--triple .price-amount { margin-top: -1px; }

  .faq-question { font-weight: 500; font-size: 18px; line-height: 18px; color: var(--grey-dark); letter-spacing: -0.2px; padding: 0 20px; }
</style>
</head>
<body>

<section class="panel panel--rooms">
  <div class="title-rule"></div>
  <h2 class="abs panel-title" style="top:79px;">Unsere Seminarräume</h2>
  <p class="abs body-text rooms-text" style="top:118px;">Für Seminare, Workshops oder Gruppentherapien können Sie einen 33 m2 großen Seminarraum sowie einen Seminarraum mit 22 m2 mieten. Der größte Seminarraum bietet einen schönen Blick auf den Sonnenwiese-Park und Sitzplätze für bis zu 20 Personen. Der kleinere Seminarraum hat ebenfalls eine komplette Fensterfront und bietet Sitzplätze für bis zu 10 Personen.</p>
  <p class="abs body-text rooms-text" style="top:262px;">Bei Bedarf können am Wochenende die Therapieräume für Kleingruppenarbeit mitgenutzt werden. Während Ihrer Veranstaltung können Sie gerne unsere Teeküche und den Verpflegungsbereich nutzen. Seminarräume stehen Ihnen grundsätzlich am Wochenende und freitags ab 15:00 Uhr zur Verfügung. Unter der Woche gerne auf Anfrage.</p>
  <p class="abs body-text rooms-text" style="top:407px;">Weiter Informationen unter:<br>www.praxis-sonnenwiese.de</p>
  <h3 class="abs room-label" style="top:452px;">Seminarraum 1</h3>
  <div class="room-photo room-photo--one" role="img" aria-label="Foto von Seminarraum 1 mit Stuhlkreis, Flipchart und Fensterfront"></div>
  <h3 class="abs room-label" style="top:631px;">Seminarraum 2</h3>
  <div class="room-photo room-photo--two" role="img" aria-label="Foto von Seminarraum 2 mit Stühlen, Bildschirm, Flipchart und Fenstern"></div>
</section>

<section class="panel panel--prices">
  <h2 class="abs panel-title" style="top:79px;">Preise der Seminarräume</h2>
  <div class="price-box" style="top:120px;">
    <div class="price-day">Freitag</div>
    <div class="price-time">15:00 bis 22:00</div>
    <div class="price-amount">150 €</div>
  </div>
  <div class="price-box" style="top:221px;">
    <div class="price-day">Samstag</div>
    <div class="price-time">8:00 bis 22:00</div>
    <div class="price-amount">220 €</div>
  </div>
  <div class="price-box" style="top:322px;">
    <div class="price-day">Sonntag</div>
    <div class="price-time">8:00 bis 20:00</div>
    <div class="price-amount">220 €</div>
  </div>
  <div class="price-box price-box--combo" style="top:423px;">
    <div class="price-day">Freitag - Samstag</div>
    <div class="price-amount">350 €</div>
  </div>
  <div class="price-box price-box--combo" style="top:524px;">
    <div class="price-day">Samstag - Sonntag</div>
    <div class="price-amount">400 €</div>
  </div>
  <div class="price-box price-box--triple" style="top:624px;">
    <div class="price-day">Freitag - Samstag -<br>Sonntag</div>
    <div class="price-amount">500 €</div>
  </div>
</section>

<section class="panel panel--faq">
  <h2 class="abs panel-title" style="top:79px;">FAQ</h2>
  <h3 class="abs faq-question" style="top:117px;">Kann ich mein Fahrrad abstellen?</h3>
  <p class="abs body-text faq-text" style="top:155px;">Abstellmöglichkeiten für Fahrräder sind vor dem Haus verfügbar.</p>
  <h3 class="abs faq-question" style="top:224px;">Wie ist die Parksituation vor Ort?</h3>
  <p class="abs body-text faq-text" style="top:262px;">Die Parkmöglichkeiten auf der Straße sind in der Innenstadt begrenzt. Es gibt aber folgende Parkhäuser in der Nähe: Parkgarage Lindenhof, Parkhaus Stadtmitte Nord, Tiefgarage Brunnenplatz, Zentral Parkhaus, Ahornhof Garage</p>
  <h3 class="abs faq-question" style="top:380px;">Warum gibt es beim Monatspaket ein Wochenlimit für die Stunden?</h3>
  <p class="abs body-text faq-text" style="top:436px;">Eine gleichmäßige Auslatung der Räume sorgt dafür, dass jeder zu attraktiven Zeiten Räume mieten kann. Diese gleichmäßige Auslatung schaffen wir durch unsere Wochenlimits.</p>
  <h3 class="abs faq-question" style="top:533px;">Wie läuft die Bezahlung ab?</h3>
  <p class="abs body-text faq-text" style="top:572px;">Sie erhalten zu Beginn eines Monats eine Rechnung über die gesamten gemieteten Stunden im vergangenen Monat. Den Rechnungsbetrag überweisen Sie auf das in der Rechnung angegebene Konto.</p>
  <h3 class="abs faq-question" style="top:685px;">Gibt es jemanden, der die Räume aufräumt?</h3>
  <p class="abs body-text faq-text" style="top:723px;">Nein, jeder Mieter sorgt dafür, dass die gemieteten Räume sauber und ordentlich hinterlassen werden.</p>
</section>

</body>
</html>
```